Design some Business Cards

Note: Designs submitted so far are too heavy. Too much bright red color. I would like to restate that I want a white business card with minimal use of red/green or any other color.

I want to create a business card for a financial advisory. Name of the company is "TelvaQuin Wealth Partners". The company advises clients on investments in global equity and real estate markets.

I want a CLEAN and MINIMALIST design. I want a white business card with a tinge of red. Don't want a coloured card.

An example of front side of the business card I have with me. Please see attached file BC1. I also need a design for the back side of the business card.
These are only examples. No need to mimic these. I am open to all designs.

Details I want on the business card as follows:

Name: Dinesh K. Varma

Designation: Advisor

Address: 612, Maple Ridge Co-operative Society,
Beside QuikBazar, Lake Road, Veltora, 400213.

Tel: (+91) 98271 53308

Website: [url removed, login to view]

Email: [url removed, login to view]@[url removed, login to view]

I want to add the following comparison of "What We Do" and "What We Don't Do" (i.e. what our competition does.)
So basically on the business card itself, I want these differences highlighted.

Here's the text:

What We Do | What We Don't Do
|
Prudent Advise | Salesy Pitches
Build Your Portfolio | Sell You Products
Focused, Principled Investing | Double-your-money-guaranteed
Comprehensive Planning | Short-term Trading

Please attached examples that I found for Dos and Don'ts. These are just examples. No need to mimic these. I am OPEN TO ALL IDEAS.

I am also attaching the logo files.

The style has to be highly professional, sophisticated and slick.
I would describe the requirement as below:

1. Trustworthy - People give us their savings to manage. Trust is essential.
2. Elegant / classy - This is a top investment management company.
3. Clean

```html
<!DOCTYPE html>
<html lang="en">
<head>
<meta charset="utf-8">
<title>TelvaQuin Wealth Partners – Business Cards</title>
<link href="https://fonts.googleapis.com/css2?family=Cinzel:wght@400;500&family=Open+Sans:wght@400;600&display=swap" rel="stylesheet">
<style>
  :root {
    --backdrop: #d9d9d9;
    --card: #fbfbfa;
    --ink: #3a3a3a;
    --ink-soft: #555555;
    --accent: #e0262b;
    --accent-faint: #f6dede;
    --serif: 'Cinzel', 'Times New Roman', serif;
    --sans: 'Open Sans', Arial, sans-serif;
  }
  * { box-sizing: border-box; margin: 0; padding: 0; }
  html, body { width: 1200px; height: 900px; overflow: hidden; }
  body { background: var(--backdrop); position: relative; font-family: var(--sans); color: var(--ink); }

  .card {
    position: absolute;
    width: 620px; height: 354px;
    background: var(--card);
    overflow: hidden;
    box-shadow: 0 6px 18px rgba(0,0,0,0.18);
  }
  .card--front { left: 120px; top: 90px; }
  .card--back  { left: 460px; top: 456px; }

  .faint-square {
    position: absolute;
    background: var(--accent-faint);
    opacity: 0.7;
  }
  .card--front .faint-square { width: 120px; height: 120px; left: -50px; top: 150px; }
  .card--back  .faint-square { width: 170px; height: 170px; right: -40px; top: -60px; }

  /* brand block */
  .brand { display: flex; align-items: center; gap: 12px; }
  .brand__mark { width: 22px; height: 22px; background: var(--accent); flex: none; }
  .brand__name {
    font-family: var(--serif); font-weight: 400; color: var(--ink);
    font-size: 25px; line-height: 1.05; letter-spacing: 1px;
  }

  .card--front .brand { position: absolute; left: 150px; top: 56px; }

  /* comparison */
  .compare {
    position: absolute; left: 60px; right: 60px; top: 150px;
    display: grid; grid-template-columns: 1fr 2px 1fr; column-gap: 14px;
  }
  .compare__divider { background: var(--accent); }
  .compare__col { font-size: 14px; line-height: 1.45; }
  .compare__col--do { text-align: right; color: var(--ink); }
  .compare__col--dont { text-align: left; color: var(--ink); }
  .compare__head {
    font-size: 16px; letter-spacing: 0.5px; margin-bottom: 6px; font-weight: 400;
  }
  .compare__col--dont .compare__head { color: var(--accent); }
  .compare__list { list-style: none; }

  /* back side */
  .person { position: absolute; left: 40px; top: 52px; }
  .person__name { font-size: 22px; letter-spacing: 0.5px; font-weight: 400; }
  .person__first { color: var(--accent); }
  .person__rest { color: var(--ink); }
  .person__role { font-size: 12px; color: var(--ink-soft); margin-top: 2px; }

  .contact { position: absolute; left: 40px; bottom: 40px; list-style: none; font-size: 13px; color: var(--ink); }
  .contact__item { display: flex; align-items: flex-start; gap: 8px; margin-top: 4px; }
  .contact__item--address { font-size: 11px; line-height: 1.35; }
  .contact__icon { width: 12px; height: 12px; flex: none; margin-top: 3px; fill: var(--accent); }

  .card--back .brand { position: absolute; right: 40px; top: 170px; }
  .card--back .brand__name { text-align: left; }
</style>
</head>
<body>

  <section class="card card--front" aria-label="Card front">
    <div class="faint-square"></div>
    <div class="brand">
      <span class="brand__mark"></span>
      <span class="brand__name">TelvaQuin<br>Wealth Partners</span>
    </div>
    <div class="compare">
      <div class="compare__col compare__col--do">
        <h2 class="compare__head">WHAT WE DO</h2>
        <ul class="compare__list">
          <li>Prudent Advise</li>
          <li>Build Your Portfolio</li>
          <li>Focused, Principled Investing</li>
          <li>Comprehensive Planning</li>
        </ul>
      </div>
      <div class="compare__divider"></div>
      <div class="compare__col compare__col--dont">
        <h2 class="compare__head">WHAT WE DON'T DO</h2>
        <ul class="compare__list">
          <li>Salesy Pitches</li>
          <li>Sell You Products</li>
          <li>Double-your-money-guaranteed</li>
          <li>Short-term Trading</li>
        </ul>
      </div>
    </div>
  </section>

  <section class="card card--back" aria-label="Card back">
    <div class="faint-square"></div>
    <div class="person">
      <h1 class="person__name"><span class="person__first">DINESH</span> <span class="person__rest">K. VARMA</span></h1>
      <p class="person__role">Advisor</p>
    </div>

    <ul class="contact">
      <li class="contact__item contact__item--address">
        <svg class="contact__icon" viewBox="0 0 12 12"><path d="M6 0a4 4 0 0 0-4 4c0 3 4 8 4 8s4-5 4-8a4 4 0 0 0-4-4zm0 5.6A1.6 1.6 0 1 1 6 2.4a1.6 1.6 0 0 1 0 3.2z"/></svg>
        <span>612, Maple Ridge Co-operative Society,<br>Beside QuikBazar, Lake Road, Veltora, 400213.</span>
      </li>
      <li class="contact__item">
        <svg class="contact__icon" viewBox="0 0 12 12"><path d="M2.4 0.6l2 2-1 1.4a7 7 0 0 0 4.6 4.6l1.4-1 2 2-1.4 1.8C5 11 1 7 0.6 2z"/></svg>
        <span>(+91) 98271 53308</span>
      </li>
      <li class="contact__item">
        <svg class="contact__icon" viewBox="0 0 12 12"><path d="M0 2h12v1.2L6 7 0 3.2z M0 4.6l6 3.8 6-3.8V10H0z"/></svg>
        <span>telvaquin.partners@mailnest.com</span>
      </li>
      <li class="contact__item">
        <svg class="contact__icon" viewBox="0 0 12 12"><circle cx="6" cy="6" r="6"/><path d="M4 3l1 1-.5.8a3.5 3.5 0 0 0 1.7 1.7L7 6l1 1-.7.9C5.5 7.8 4 6.3 3.2 4.2z" fill="#fbfbfa"/></svg>
        <span>(+91) 98271 53308</span>
      </li>
    </ul>

    <div class="brand">
      <span class="brand__mark"></span>
      <span class="brand__name">TelvaQuin<br>Wealth Partners</span>
    </div>
  </section>

</body>
</html>
```